K-VOR Landing Page

We want to re-design our current home page on our website (www.plexamora.com) to simplify it and reduce it down to the (3) main products / services we offer. There are too many options of where they can go and it seems to be confusing for them. Additionally, we sell a higher end software product and we want the site to appear very professional for when CFO's considering our software can be confident in its quality and the long established company that we are. Our products and services are all about optimizing manufacturing production for sheet metal stampers (primarily automotive and appliance). I am including a rough power point layout of what we are thinking along with flyers for our three main products. We want to maintain the look and feel of the sample marketing materials as much as possible but does not have to match exactly. We will be producing the video ourselves to add where the power point shows a video being. Please review our website for any additional information.

```html
<!DOCTYPE html>
<html lang="en">
<head>
<meta charset="utf-8">
<title>K-VOR Solutions</title>
<link href="https://fonts.googleapis.com/css2?family=Poppins:wght@400;500;600;700&display=swap" rel="stylesheet">
<style>
:root{
  --navy:#1e566b;
  --navy-dark:#1a4b5e;
  --slate:#4a7a89;
  --yellow:#fdc51a;
  --ink:#111111;
  --text:#1f1f1f;
  --white:#ffffff;
  --black:#000000;
  --line:#d6d6d6;
}
*{margin:0;padding:0;box-sizing:border-box}
html,body{width:832px;height:1200px;overflow:hidden;background:var(--white)}
body{font-family:'Poppins',sans-serif;color:var(--text);position:relative}
.abs{position:absolute}

/* header */
.brand{left:59px;top:20px;display:flex;align-items:center;gap:8px}
.brand-mark{width:16px;height:16px;background:var(--yellow)}
.brand-name{font-size:30px;font-weight:700;color:#3a3a3a;letter-spacing:1px;line-height:1}
.call{left:635px;top:25px;display:flex;align-items:center;gap:6px}
.call-icon{width:31px;height:31px;border-radius:50%;background:var(--yellow);display:flex;align-items:center;justify-content:center}
.call-label{font-size:10px;color:var(--navy);line-height:1.2}
.call-number{font-size:14.5px;font-weight:600;color:var(--ink);line-height:1.2}

.nav{left:0;top:76px;width:832px;height:34px;background:var(--navy-dark)}
.nav span{position:absolute;top:9px;font-size:10px;color:var(--white);white-space:nowrap}
.nav i{position:absolute;top:13px;width:1px;height:14px;background:var(--white)}
.caret{display:inline-block;width:5px;height:5px;border-right:1px solid var(--yellow);border-bottom:1px solid var(--yellow);transform:rotate(45deg);margin-left:4px;position:relative;top:-2px}

/* hero */
.hero{left:0;top:110px;width:832px;height:312px;background:var(--navy)}
.hero-title{left:59px;top:187px;font-size:24px;font-weight:600;color:var(--white);white-space:nowrap}
.hero-title em{font-style:normal;color:var(--yellow)}
.hero-copy{left:59px;top:234px;width:315px;font-size:9.4px;line-height:13.9px;color:var(--white)}
.video{left:425px;top:155px;width:335px;height:223px;background:linear-gradient(135deg,#6f7b7d 0%,#a9a9a2 45%,#8b8f8c 100%)}
.play{left:576px;top:249px;width:35px;height:35px;border-radius:50%;background:var(--white);display:flex;align-items:center;justify-content:center}
.hero-edge{left:0;top:415px}

/* cards */
.card{top:494px;width:231px;height:340px}
.card svg{position:absolute;left:0;top:0}
.card-title{position:absolute;left:0;width:231px;text-align:center;font-size:13.6px;font-weight:600;line-height:20.8px;text-transform:uppercase}
.card-btn{position:absolute;left:66px;top:111px;width:97px;height:27px;font-size:9px;font-weight:500;display:flex;align-items:center;justify-content:center;text-transform:uppercase}
.card-copy{position:absolute;left:22px;top:198px;width:196px;text-align:center;font-size:9.6px;line-height:13.9px;color:var(--text)}

/* guarantee */
.guarantee{left:0;top:898px;width:832px;height:112px;background:var(--yellow)}
.g-title{left:59px;top:944px;font-size:22px;font-weight:600;color:var(--white);white-space:nowrap}
.g-copy{left:349px;top:935px;width:390px;font-size:12.4px;line-height:17.5px;color:var(--ink);font-weight:500}

/* footer */
.footer{left:0;top:1010px;width:832px;height:190px;background:var(--black)}
.f-brand{left:64px;top:1040px;display:flex;align-items:center;gap:8px}
.f-brand .brand-name{color:var(--white);font-size:27px}
.f-note{left:59px;top:1095px;width:190px;font-size:8.2px;line-height:12.2px;color:var(--white)}
.f-item{left:340px;display:flex;gap:6px}
.f-icon{width:20px;height:20px;border-radius:50%;background:var(--yellow);display:flex;align-items:center;justify-content:center;flex:none;margin-top:2px}
.f-label{font-size:8.4px;font-weight:600;color:var(--yellow);line-height:11px}
.f-text{font-size:8.4px;color:var(--white);line-height:12px}
.f-links{left:636px;font-size:8.4px;color:var(--white)}
</style>
</head>
<body>

<header>
  <div class="abs brand"><span class="brand-mark"></span><span class="brand-name">K-VOR</span></div>
  <div class="abs call">
    <div class="call-icon">
      <svg width="15" height="15" viewBox="0 0 24 24"><path d="M6.6 10.8a15.1 15.1 0 0 0 6.6 6.6l2.2-2.2a1 1 0 0 1 1-.25 11.4 11.4 0 0 0 3.6.57 1 1 0 0 1 1 1V20a1 1 0 0 1-1 1A17 17 0 0 1 3 4a1 1 0 0 1 1-1h3.5a1 1 0 0 1 1 1c0 1.25.2 2.45.57 3.57a1 1 0 0 1-.25 1z" fill="#1e566b"/></svg>
    </div>
    <div>
      <div class="call-label">Call Us Today</div>
      <div class="call-number">555-014-2730</div>
    </div>
  </div>
</header>

<nav class="abs nav">
  <span style="left:88px">About</span><i style="left:132px"></i>
  <span style="left:142px">How We Help</span><i style="left:219px"></i>
  <span style="left:232px">K-VOR Sofware<b class="caret"></b></span><i style="left:315px"></i>
  <span style="left:328px">Transfer Press Simulation Service</span><i style="left:502px"></i>
  <span style="left:514px">Business Case<b class="caret"></b></span><i style="left:602px"></i>
  <span style="left:615px">Resources</span><i style="left:679px"></i>
  <span style="left:691px">Contact</span>
</nav>

<section>
  <div class="abs hero"></div>
  <h1 class="abs hero-title">Welcome to <em>K-VOR Solutions</em></h1>
  <p class="abs hero-copy">At our core, we are a software company committed to providing cutting-edge simulation and optimization solutions. However, we understand that our customers have diverse needs and requirements which may not fit with buying software at this time. That’s why we offer flexible options for you to experience the power of K-VOR.</p>
  <div class="abs video" role="img" aria-label="Video still of a customer giving a testimonial interview"></div>
  <div class="abs play"><svg width="14" height="16" viewBox="0 0 14 16"><path d="M2 1 L13 8 L2 15 Z" fill="#e81c1c"/></svg></div>
  <svg class="abs hero-edge" width="832" height="50" viewBox="0 0 832 50">
    <polygon points="0,6 416,37 832,6 832,16 416,47 0,16" fill="#fdc51a"/>
    <polygon points="0,0 832,0 832,6 416,37 0,6" fill="#1e566b"/>
  </svg>
</section>

<section>
  <div class="abs card" style="left:59px">
    <svg width="231" height="340" viewBox="0 0 231 340">
      <path d="M0.5,152 L0.5,320 Q0.5,328 10,329.5 L115.5,339 L221,329.5 Q230.5,328 230.5,320 L230.5,152" fill="#fff" stroke="#d6d6d6"/>
      <polygon points="0,147 115.5,165 231,147 231,157 115.5,176 0,157" fill="#1e566b"/>
      <polygon points="0,0 231,0 231,147 115.5,165 0,147" fill="#fdc51a"/>
    </svg>
    <div class="card-title" style="top:50px;color:var(--ink)">New tool simulation<br>and optimization</div>
    <div class="card-btn" style="background:var(--navy);color:var(--white)">Request a quote</div>
    <p class="card-copy">Are you starting a new transfer tooling program soon? Trust the experts at K-VOR to make it the best one you’ve ever had! Know your production rates before you build and confidently launch your tooling at the HIGHEST possible production rates!</p>
  </div>

  <div class="abs card" style="left:302px">
    <svg width="231" height="340" viewBox="0 0 231 340">
      <path d="M0.5,152 L0.5,320 Q0.5,328 10,329.5 L115.5,339 L221,329.5 Q230.5,328 230.5,320 L230.5,152" fill="#fff" stroke="#d6d6d6"/>
      <polygon points="0,147 115.5,165 231,147 231,157 115.5,176 0,157" fill="#fdc51a"/>
      <polygon points="0,0 231,0 231,147 115.5,165 0,147" fill="#1e566b"/>
    </svg>
    <div class="card-title" style="top:36px;color:var(--white)">Existing tool<br>optimization (with or<br>without CAD)</div>
    <div class="card-btn" style="background:var(--yellow);color:var(--ink)">Request a quote</div>
    <p class="card-copy">Are you at capacity in your transfer press, running your equipment harder than you’d like, or simply know you can be doing better? Our existing tool optimization service is a great way increase your production efficiency (OEE) and free up press capacity.</p>
  </div>

  <div class="abs card" style="left:544px;top:495px">
    <svg width="231" height="340" viewBox="0 0 231 340">
      <path d="M0.5,152 L0.5,320 Q0.5,328 10,329.5 L115.5,339 L221,329.5 Q230.5,328 230.5,320 L230.5,152" fill="#fff" stroke="#d6d6d6"/>
      <polygon points="0,147 115.5,165 231,147 231,157 115.5,176 0,157" fill="#1e566b"/>
      <polygon points="0,0 231,0 231,147 115.5,165 0,147" fill="#4a7a89"/>
    </svg>
    <div class="card-title" style="top:50px;color:var(--white)">K-VOR software<br>products</div>
    <div class="card-btn" style="background:var(--navy);color:var(--white)">Request a quote</div>
    <p class="card-copy">Without question, our most successful customers are the ones who use the software themselves. K-VOR Users typically see as much as 40% increase in their production rates! Hard to believe? Try it and see for yourself!</p>
  </div>
</section>

<section>
  <div class="abs guarantee"></div>
  <svg class="abs" style="left:0;top:898px" width="320" height="112" viewBox="0 0 320 112">
    <polygon points="0,0 270,0 316,57 273,112 0,112" fill="#1e566b"/>
  </svg>
  <h2 class="abs g-title">OUR GAURANTEE</h2>
  <p class="abs g-copy">You’ll make your money back in your first (5) projects or we’ll refund the entire purchase price!</p>
</section>

<footer>
  <div class="abs footer"></div>
  <div class="abs f-brand"><span class="brand-mark"></span><span class="brand-name">K-VOR</span></div>
  <p class="abs f-note">K-VOR® Solutions is a division of Northway Design Services, LLC.<br>K-VOR® is a federally registered trademark of Northway Design Service, LLC.</p>

  <div class="abs f-item" style="top:1045px">
    <div class="f-icon"><svg width="11" height="11" viewBox="0 0 24 24"><path d="M12 2a7 7 0 0 0-7 7c0 5 7 13 7 13s7-8 7-13a7 7 0 0 0-7-7z" fill="none" stroke="#111" stroke-width="2"/><circle cx="12" cy="9" r="2.5" fill="none" stroke="#111" stroke-width="2"/></svg></div>
    <div><div class="f-label">Address</div><div class="f-text">&nbsp;PO Box 412 · 318 Harlow Industrial<br>&nbsp;Dr. · Greenfield, MI 49000-0412</div></div>
  </div>
  <div class="abs f-item" style="top:1088px">
    <div class="f-icon"><svg width="11" height="11" viewBox="0 0 24 24"><path d="M6.6 10.8a15.1 15.1 0 0 0 6.6 6.6l2.2-2.2a1 1 0 0 1 1-.25 11.4 11.4 0 0 0 3.6.57 1 1 0 0 1 1 1V20a1 1 0 0 1-1 1A17 17 0 0 1 3 4a1 1 0 0 1 1-1h3.5a1 1 0 0 1 1 1c0 1.25.2 2.45.57 3.57a1 1 0 0 1-.25 1z" fill="none" stroke="#111" stroke-width="2"/></svg></div>
    <div><div class="f-label">Phone</div><div class="f-text">555-014-2730 &nbsp;Fax: 555-014-2733</div></div>
  </div>
  <div class="abs f-item" style="top:1121px">
    <div class="f-icon"><svg width="11" height="11" viewBox="0 0 24 24"><rect x="3" y="5" width="18" height="14" rx="2" fill="none" stroke="#111" stroke-width="2"/><path d="M3 7l9 6 9-6" fill="none" stroke="#111" stroke-width="2"/></svg></div>
    <div><div class="f-label">Email</div><div class="f-text">info@plexamora.com</div></div>
  </div>

  <div class="abs f-links" style="top:1050px">Simulation Defined</div>
  <div class="abs f-links" style="top:1069px">Privacy Policy</div>
  <div class="abs f-links" style="top:1092px">Sitemap</div>
</footer>

</body>
</html>
```